Business card design for new eCommerce site focusing on integrity and strong businsess tactics

We need a business card that will stand out and be memorable. Something with color that matches our company logo colors. Think high end version of Dealvine. There are 2 logos provided. The parent company is called Bright Harbor Ventures and we are presenting a new and very exciting eCommerce site called KeenTraders.example.

Target Market(s)

Our target markets are in the Activities, Food and Beverage, Health and Beauty

Industry/Entity Type

Marketing

Contact Information for Business Card

We have 4 members that need cards...I will provide all info to the winner of the design contest
Business Address is
48730 West 61st Avenue, Suite C204
Phoenix AZ 85917

Font styles to use
Serif
Sans Serif

Colors

Designer to choose colors to be used in the design.

Requirements
Must have
• The card must be memorable...should be unique in design but must exude integrity and be playful .
• I have provided several colors or our parent company...please feel free to use which ever
Nice to have
• I will leave this up to you. Feel free to use other images of your choosing that wraps around our client.....Activities, Dining, Health, Beauty
Should not have
• just dont be boring

```html
<!DOCTYPE html>
<html lang="en">
<head>
<meta charset="UTF-8">
<title>Bright Harbor Ventures – Business Card</title>
<link rel="stylesheet" href="https://fonts.googleapis.com/css2?family=Poppins:wght@600&family=Tinos:wght@400;700&display=swap">
<style>
  :root {
    --page-bg: #ffffff;
    --card-bg: #232323;
    --brand-green: #a6ce39;
    --partner-blue: #2a7fc1;
    --text-light: #d6d6d6;
    --text-muted: #c4c4c4;
  }
  html, body {
    margin: 0;
    padding: 0;
    width: 1200px;
    height: 691px;
    overflow: hidden;
    background: var(--page-bg);
  }
  .canvas {
    position: relative;
    width: 1200px;
    height: 691px;
  }
  .card {
    position: absolute;
    top: 180px;
    width: 512px;
    height: 312px;
    border-radius: 31px;
    background: var(--card-bg);
    overflow: hidden;
  }
  .card--front { left: 60px; }
  .card--back { left: 622px; }

  .brand-mark {
    position: absolute;
    border: 3px solid var(--brand-green);
    border-radius: 50%;
    box-sizing: border-box;
  }
  .brand-name {
    position: absolute;
    margin: 0;
    font-family: "Poppins", sans-serif;
    font-weight: 600;
    color: var(--brand-green);
    white-space: nowrap;
    transform: translateX(-50%);
  }

  .card--front .brand-mark {
    left: 230px; top: 86px; width: 52px; height: 52px;
  }
  .card--front .brand-name {
    left: 256px; top: 152px; font-size: 24px;
  }

  .partner {
    position: absolute;
    left: 444px;
    top: 80px;
    width: 20px;
    height: 170px;
  }
  .partner-name {
    position: absolute;
    left: 50%;
    top: 0;
    font-family: "Poppins", sans-serif;
    font-weight: 600;
    font-size: 12px;
    color: var(--partner-blue);
    writing-mode: vertical-rl;
    transform: translateX(-50%) rotate(180deg);
    white-space: nowrap;
  }
  .partner-dot {
    position: absolute;
    left: 3px;
    bottom: 0;
    width: 14px;
    height: 14px;
    border-radius: 50%;
    background: var(--partner-blue);
  }

  .card--back .brand-mark {
    left: 117px; top: 128px; width: 42px; height: 42px;
  }
  .card--back .brand-name {
    left: 138px; top: 186px; font-size: 17px;
  }

  .contact-person {
    position: absolute;
    left: 302px;
    top: 30px;
    font-family: "Tinos", serif;
  }
  .person-name {
    margin: 0;
    font-weight: 700;
    font-size: 20px;
    color: var(--text-light);
  }
  .person-title {
    margin: 3px 0 0;
    font-size: 15px;
    color: var(--text-muted);
  }

  .contact-list {
    position: absolute;
    left: 284px;
    margin: 0;
    padding: 0;
    list-style: none;
    font-family: "Tinos", serif;
    font-size: 15px;
    line-height: 19px;
    color: var(--text-light);
  }
  .contact-list--address { top: 136px; }
  .contact-list--reach { top: 223px; }
  .contact-list li {
    position: relative;
    padding-left: 18px;
    margin-bottom: 4px;
  }
  .contact-icon {
    position: absolute;
    left: 0;
    top: 3px;
    width: 12px;
    height: 12px;
    fill: var(--text-light);
  }
</style>
</head>
<body>
<div class="canvas">

  <section class="card card--front">
    <span class="brand-mark"></span>
    <p class="brand-name">Bright Harbor Ventures</p>
    <div class="partner">
      <span class="partner-name">KeenTraders.example</span>
      <span class="partner-dot"></span>
    </div>
  </section>

  <section class="card card--back">
    <span class="brand-mark"></span>
    <p class="brand-name">Bright Harbor Ventures</p>

    <div class="contact-person">
      <p class="person-name">Marcus Ellery</p>
      <p class="person-title">Manager</p>
    </div>

    <ul class="contact-list contact-list--address">
      <li>
        <svg class="contact-icon" viewBox="0 0 12 12" aria-hidden="true"><path d="M6 0a4 4 0 0 0-4 4c0 3 4 8 4 8s4-5 4-8a4 4 0 0 0-4-4zm0 5.6A1.6 1.6 0 1 1 6 2.4a1.6 1.6 0 0 1 0 3.2z"/></svg>
        48730 West 61st Avenue<br>Suite C204<br>Phoenix AZ 85917
      </li>
    </ul>

    <ul class="contact-list contact-list--reach">
      <li>
        <svg class="contact-icon" viewBox="0 0 12 12" aria-hidden="true"><path d="M2.4 0.6l1.8 0 0.8 2.6-1.2 1a7 7 0 0 0 3 3l1-1.2 2.6 0.8 0 1.8c0 .8-.6 1.4-1.4 1.4A9.6 9.6 0 0 1 1 1.9C1 1.2 1.6 .6 2.4 .6z"/></svg>
        +1 555 014 2290
      </li>
      <li>
        <svg class="contact-icon" viewBox="0 0 12 12" aria-hidden="true"><path d="M0 2.5h12v7H0z M0.8 3.2 6 6.8l5.2-3.6" stroke="#232323" stroke-width="0.9"/></svg>
        marcus@brightharbor.example
      </li>
      <li>
        <svg class="contact-icon" viewBox="0 0 12 12" aria-hidden="true"><circle cx="6" cy="6" r="5.6"/><path d="M0.6 6h10.8M6 0.4c-2.6 3-2.6 8.2 0 11.2M6 0.4c2.6 3 2.6 8.2 0 11.2" stroke="#232323" stroke-width="0.8" fill="none"/></svg>
        www.brightharbor.example
      </li>
    </ul>
  </section>

</div>
</body>
</html>
```